Web design for Home Sleep Study clinic

We´re a group of Phisicians and working with patients with snoring e sleep apnea problems.
We´re beginning to offer home sleep studies (an option to lab studies) and we ´re building a webpage to share information, to find patients and to offer our product.
We already have a www adress and some idea about logo and brand.
We´re in Brazil and our service/webpage will be in Portuguese.

```html
<!DOCTYPE html>
<html lang="pt">
<head>
<meta charset="utf-8">
<title>Nocturna Saúde</title>
<link href="https://fonts.googleapis.com/css2?family=Figtree:wght@400;500;600&display=swap" rel="stylesheet">
<style>
  :root {
    --blue: #1b8fc9;
    --blue-dark: #1a77c0;
    --ink: #333333;
    --muted: #666666;
    --panel-grey: #ebebeb;
    --footer: #3b3b3b;
    --footer-text: #e2e2e2;
    --field-border: #d4d4d4;
  }
  * { box-sizing: border-box; margin: 0; padding: 0; }
  html, body { width: 1200px; height: 1173px; overflow: hidden; }
  body {
    position: relative;
    background: #ffffff;
    font-family: "Figtree", "Helvetica Neue", Arial, sans-serif;
    color: var(--ink);
  }
  a { color: inherit; text-decoration: none; }

  /* Header */
  .site-header { position: absolute; left: 0; top: 0; width: 1200px; height: 104px; }
  .brand {
    position: absolute; left: 190px; top: 48px;
    font-size: 19px; font-weight: 600; color: var(--ink); letter-spacing: 0.2px;
    display: flex; align-items: center; gap: 9px;
  }
  .brand-mark { width: 12px; height: 12px; background: var(--blue); }
  .main-nav { position: absolute; top: 45px; left: 0; font-size: 13px; font-weight: 500; }
  .main-nav a { position: absolute; white-space: nowrap; color: #222; }
  .main-nav a.active { color: var(--blue); }
  .main-nav .caret { display: inline-block; margin-left: 3px; vertical-align: 1px; }
  .header-rule { position: absolute; left: 176px; top: 100px; width: 847px; height: 3px; background: var(--blue); }

  /* Hero */
  .hero { position: absolute; left: 0; top: 103px; width: 1200px; height: 474px; overflow: hidden; }
  .hero-photo {
    position: absolute; left: 80px; top: 0; width: 900px; height: 474px;
    background:
      radial-gradient(ellipse 60% 70% at 45% 60%, rgba(196,162,140,0.55), rgba(196,162,140,0) 70%),
      radial-gradient(ellipse 55% 60% at 70% 40%, rgba(150,178,208,0.75), rgba(150,178,208,0) 75%),
      linear-gradient(90deg, #ffffff 0%, #eef0f2 18%, #e3e8ee 45%, #cdd8e4 70%, #f4f6f8 100%);
  }
  .hero-photo::after {
    content: ""; position: absolute; inset: 0;
    background: linear-gradient(90deg, #fff 0%, rgba(255,255,255,0) 14%, rgba(255,255,255,0) 88%, #fff 100%),
                linear-gradient(180deg, rgba(255,255,255,0.5) 0%, rgba(255,255,255,0) 25%);
  }
  .signup-card {
    position: absolute; left: 685px; top: 61px; width: 308px; height: 342px;
    background: #ffffff; border-top: 4px solid var(--blue);
  }
  .signup-title {
    position: absolute; left: 20px; top: 30px;
    font-size: 16.5px; font-weight: 600; color: var(--blue); letter-spacing: 0.1px;
  }
  .field {
    position: absolute; left: 19px; width: 264px; height: 39px;
    border: 1px solid var(--field-border); border-radius: 3px;
    background: linear-gradient(#ffffff, #f4f4f4);
    font-size: 11.5px; color: #8a8a8a; padding: 0 15px; line-height: 37px;
  }
  .field-select::after {
    content: ""; position: absolute; right: 15px; top: 16px;
    border-left: 4.5px solid transparent; border-right: 4.5px solid transparent; border-top: 5px solid #9a9a9a;
  }
  .register-btn {
    position: absolute; left: 19px; top: 281px; width: 264px; height: 38px;
    border-radius: 3px; background: linear-gradient(#2a93d6, var(--blue-dark));
    color: #fff; font-size: 13px; font-weight: 600; text-align: center; line-height: 38px; letter-spacing: 0.3px;
  }

  /* Info band */
  .info-band { position: absolute; left: 0; top: 577px; width: 1200px; height: 320px; background: var(--panel-grey); }
  .slider-arrows { position: absolute; left: 998px; top: 41px; }
  .info-col { position: absolute; top: 76px; }
  .info-col h2 { font-size: 16.5px; font-weight: 500; color: #2b2b2b; letter-spacing: 0.1px; }
  .info-col p { margin-top: 10px; font-size: 12.2px; line-height: 20.6px; color: var(--muted); text-align: justify; letter-spacing: -0.15px; }
  .info-col.signs { left: 180px; width: 494px; }
  .info-col.about { left: 715px; width: 302px; }
  .info-col.about p { letter-spacing: -0.3px; }

  /* Footer */
  .footer-rule { position: absolute; left: 0; top: 897px; width: 1200px; height: 4px; background: var(--blue); }
  .site-footer { position: absolute; left: 0; top: 901px; width: 1200px; height: 272px; background: var(--footer); color: var(--footer-text); }
  .footer-col { position: absolute; top: 34px; }
  .footer-col h3 { font-size: 13.5px; font-weight: 600; color: #fff; }
  .footer-col ul { list-style: none; margin-top: 14px; }
  .footer-col li { font-size: 11px; line-height: 24px; letter-spacing: 0.2px; }
  .footer-col address { font-style: normal; margin-top: 13px; font-size: 11.3px; line-height: 19px; }
  .col-sitemap { left: 195px; }
  .col-links { left: 320px; }
  .col-address { left: 799px; }
  .footer-divider { position: absolute; left: 171px; top: 205px; width: 858px; height: 1px; background: #2c2c2c; box-shadow: 0 1px 0 #4a4a4a; }
  .copyright { position: absolute; left: 196px; top: 228px; font-size: 12px; letter-spacing: 0.4px; }
  .follow { position: absolute; left: 821px; top: 225px; font-size: 12px; display: flex; align-items: center; }
  .follow span { margin-right: 12px; }
  .social { width: 27px; height: 27px; border: 2px solid #9a9a9a; border-radius: 50%; margin-right: 12px; }
</style>
</head>
<body>

<header class="site-header">
  <div class="brand"><span class="brand-mark"></span>Nocturna Saúde</div>
  <nav class="main-nav">
    <a href="#" style="left:522px">ABOUT US</a>
    <a href="#" style="left:611px">SNORING</a>
    <a href="#" class="active" style="left:693px">TREATMENTS<svg class="caret" width="7" height="5" viewBox="0 0 7 5"><path d="M0.5 0.5 L3.5 3.8 L6.5 0.5" fill="none" stroke="#1b8fc9" stroke-width="1.3"/></svg></a>
    <a href="#" style="left:799px">PROFFESIONALS</a>
    <a href="#" style="left:921px">CONTACT US</a>
  </nav>
  <div class="header-rule"></div>
</header>

<section class="hero">
  <div class="hero-photo" role="img" aria-label="Photograph of a man asleep in bed on a white pillow, in soft blue and white tones"></div>
  <form class="signup-card">
    <h1 class="signup-title">HELP ME TO SLEEP BETTER</h1>
    <div class="field" style="top:74px">Full Name</div>
    <div class="field" style="top:123px">Email</div>
    <div class="field" style="top:172px">Phone</div>
    <div class="field field-select" style="top:220px">Location</div>
    <div class="register-btn">REGISTER</div>
  </form>
</section>

<section class="info-band">
  <svg class="slider-arrows" width="26" height="12" viewBox="0 0 26 12" aria-label="Previous and next">
    <path d="M8 1 L3 6 L8 11" fill="none" stroke="#777" stroke-width="2.6"/>
    <path d="M18 1 L23 6 L18 11" fill="none" stroke="#777" stroke-width="2.6"/>
  </svg>
  <article class="info-col signs">
    <h2>SIGNS AND SYMPTOMS OF OBSTRUCTIVE&nbsp; SLEEP APNEA</h2>
    <p>Lorem ipsum dolor sit amet, consectetur adipiscing elit. Vivamus orci lectus, auctor eu venenatis quis, commodo id ligula. Donec urna massa, aliquam euismod tincidunt id, euismod in augue. Mauris lobortis commodo ligula, vel placerat erat tempor adipiscing. Vestibulum vel velit ante. Suspendisse potenti. Sed neque eros, rutrum eget elementum sit amet, mollis non ante. Nunc eget viverra dolor. Proin vitae ornare felis. Vestibulum viverra bibendum velit,</p>
  </article>
  <article class="info-col about">
    <h2>WHAT IS SLEEPAPNEA</h2>
    <p>Sleep apnea is a condition of temporary closure of the upper respiratory passage during sleep. It can lead to serious life long complications which are preventable through treatment.&nbsp; In Sleep Lab, monitoring is done by Pulmonlogists. We have facility for CPAP titration also</p>
  </article>
</section>

<div class="footer-rule"></div>
<footer class="site-footer">
  <div class="footer-col col-sitemap">
    <h3>SITEMAP</h3>
    <ul><li>ABOUT US</li><li>SNORING</li><li>TREATMENTS</li><li>DOCTORS</li><li>CONTACT US</li></ul>
  </div>
  <div class="footer-col col-links">
    <h3>USEFUL LINKS</h3>
    <ul><li>ENQUIRY</li><li>BOOK ONLINE</li><li>WHY US</li><li>LOCATE US</li></ul>
  </div>
  <div class="footer-col col-address">
    <h3>OUR ADDRESS</h3>
    <address>Donec eu lacus vitae<br>D-304 Purus dapibus egestas<br>Near nec a mauris.<br>Tel: +000 123456789<br>Fax: +000 123456789</address>
  </div>
  <div class="footer-divider"></div>
  <div class="copyright">© 2014 Nocturna Saúde. All Rights Reserved</div>
  <div class="follow">
    <span>Follow us on</span>
    <div class="social" role="img" aria-label="Social network link"></div>
    <div class="social" role="img" aria-label="Social network link"></div>
    <div class="social" role="img" aria-label="Social network link"></div>
  </div>
</footer>

</body>
</html>
```